Customs House descriptive business cards

We require a two-sided business card that has a simple yet elegant design. We want to be able to promote our services as a customs house. This card should include our logo, contact info and services offered with the logo being on one side and the contact info and services on the flip side

Target Market(s)

Importers / exporters to and from the Bahamas

Industry/Entity Type

Logistics

Contact Information for Business Card

The front side of the card could have the logo and the flip side should have the other relevant info

Font styles to use
Serif

Colors

Designer to choose colors to be used in the design.

Requirements
Must have
• (Kelpway Brokers Ltd) Logo, address and contact info also services:
• import customs clearance, Delivery & HAndling services,Florida pickups, Export packing & Crating Services, export customs clearance, Consulting

```html
<!DOCTYPE html>
<html lang="en">
<head>
<meta charset="utf-8">
<title>Kelpway Brokers Ltd. – Business Card</title>
<link rel="stylesheet" href="https://fonts.googleapis.com/css2?family=Poppins:wght@400;500;600&display=swap">
<style>
  :root {
    --page-bg: #ecebe8;
    --card-white: #ffffff;
    --brand-blue: #1f78c8;
    --brand-blue-deep: #1565c0;
    --brand-blue-light: #2a98dc;
    --ink: #3a3a3a;
    --ink-soft: #555b61;
    --icon: #4a5560;
    --logo-pale: #dfe5ea;
    --services-ink: #eef5fc;
  }
  * { box-sizing: border-box; margin: 0; padding: 0; }
  html, body { width: 1200px; height: 920px; overflow: hidden; }
  body {
    background: var(--page-bg);
    position: relative;
    font-family: "Poppins", sans-serif;
  }
  .card {
    position: absolute;
    top: 314px;
    width: 536px;
    height: 300px;
    box-shadow: 0 6px 18px rgba(0,0,0,0.18);
  }

  /* Contact side */
  .card--contact { left: 46px; background: var(--card-white); }
  .brand-name {
    position: absolute;
    left: 20px; top: 150px;
    width: 250px;
    text-align: center;
    font-family: "Poppins", sans-serif;
    font-weight: 500;
    color: var(--brand-blue);
    line-height: 1.15;
  }
  .brand-name__main { display: block; font-size: 30px; letter-spacing: 1px; }
  .brand-name__sub { display: block; font-size: 13px; letter-spacing: 4px; margin-top: 2px; }
  .divider {
    position: absolute;
    left: 265px; top: 67px;
    width: 2px; height: 165px;
    background: var(--brand-blue);
  }
  .person {
    position: absolute;
    left: 290px; top: 62px;
  }
  .person__name {
    font-size: 17px; font-weight: 600;
    color: var(--brand-blue); letter-spacing: 0.6px;
    line-height: 22px;
  }
  .person__role {
    font-size: 10.5px; color: var(--ink-soft);
    letter-spacing: 0.4px; margin-top: 2px;
  }
  .contact-list {
    position: absolute;
    left: 290px; top: 121px;
    list-style: none;
  }
  .contact-list li {
    display: flex; align-items: center;
    height: 18.6px;
    font-size: 12px; color: var(--ink);
    letter-spacing: 0.3px;
  }
  .contact-list svg { width: 10px; height: 10px; margin-right: 10px; flex: none; }
  .address {
    position: absolute;
    left: 0; right: 0; top: 258px;
    text-align: center;
    font-size: 10.5px; color: var(--ink);
    letter-spacing: 0.4px;
  }

  /* Logo & services side */
  .card--services {
    left: 630px;
    background: linear-gradient(120deg, var(--brand-blue-deep) 0%, var(--brand-blue) 50%, var(--brand-blue-light) 100%);
  }
  .brand-name--reverse {
    left: 0; right: 0; top: 160px; width: auto;
    color: var(--logo-pale);
  }
  .services {
    position: absolute;
    left: 0; right: 0; top: 240px;
    text-align: center;
    font-size: 11.5px;
    color: var(--services-ink);
    letter-spacing: 0.3px;
    line-height: 19px;
  }
  .services span { white-space: nowrap; }
  .services span::before {
    content: ""; display: inline-block;
    width: 5px; height: 5px;
    background: var(--services-ink);
    margin: 0 6px 1px 8px;
    vertical-align: middle;
  }
</style>
</head>
<body>

<section class="card card--contact">
  <div class="brand-name">
    <span class="brand-name__main">KELPWAY</span>
    <span class="brand-name__sub">BROKERS LTD.</span>
  </div>
  <div class="divider"></div>
  <div class="person">
    <p class="person__name">MARCUS DELANE</p>
    <p class="person__role">OPERATIONS DIRECTOR</p>
  </div>
  <ul class="contact-list">
    <li><svg viewBox="0 0 10 10"><path d="M2 0.5 L3.6 2.6 L2.7 3.6 Q3.8 5.9 6.2 7.2 L7.3 6.3 L9.5 7.9 L8.4 9.5 Q2.5 8.6 0.5 1.6 Z" fill="#4a5560"/></svg>(242) 555-0147 (OFFICE)</li>
    <li><svg viewBox="0 0 10 10"><rect x="2.5" y="0.5" width="5" height="9" rx="1" fill="none" stroke="#4a5560" stroke-width="1"/><circle cx="5" cy="8" r="0.6" fill="#4a5560"/></svg>(242) 555-0193 (CELL)</li>
    <li><svg viewBox="0 0 10 10"><rect x="0.5" y="2" width="9" height="6.5" fill="none" stroke="#4a5560" stroke-width="1"/><path d="M0.5 2 L5 5.6 L9.5 2" fill="none" stroke="#4a5560" stroke-width="1"/></svg>imports@kelpwaybrokers.com</li>
    <li><svg viewBox="0 0 10 10"><circle cx="5" cy="5" r="4.4" fill="none" stroke="#4a5560" stroke-width="1"/><ellipse cx="5" cy="5" rx="1.9" ry="4.4" fill="none" stroke="#4a5560" stroke-width="0.8"/><path d="M0.6 5 H9.4" stroke="#4a5560" stroke-width="0.8"/></svg>www.kelpwaybrokers.com</li>
    <li><svg viewBox="0 0 10 10"><circle cx="5" cy="5" r="4.4" fill="#4a5560"/></svg>@kelpwaybrokers</li>
    <li><svg viewBox="0 0 10 10"><circle cx="5" cy="5" r="4.4" fill="#4a5560"/></svg>@kelpwaybrokers</li>
  </ul>
  <p class="address">#42 CORAL RIDGE ROAD P.O. BOX SP-40217 NASSAU, BAHAMAS</p>
</section>

<section class="card card--services">
  <div class="brand-name brand-name--reverse">
    <span class="brand-name__main">KELPWAY</span>
    <span class="brand-name__sub">BROKERS LTD.</span>
  </div>
  <p class="services">
    <span>import customs clearance</span> <span>Delivery &amp; HAndling services</span> <span>Florida pickups</span><br>
    <span>Export packing &amp; Crating Services</span> <span>export customs clearance</span> <span>Consulting</span>
  </p>
</section>

</body>
</html>
```